Not another boring Business Card Design Project

This is not another boring Business Card Design Project.

We are looking for the weirdest, wackiest most boundary pushing designs that you can come up with.

If you believe that design can be fun, energetic, crazy, unpredictable, beautiful and eye-catching then read on… this project is for you.

We are Wendel Prask and we print plastic cards.

We are running a Plastic Card Design Competition.

And we need a plastic card to advertise the competition to graphic designers just like you.

The design needs to make your average designers’ jaws drop and their eyes pop out.

You can do what you wish with the card design, so long as it stands out.

We like these designs, designs that stretch the boundaries and become something beyond just another business card:

http://quorvexpixels.net/wp-content/uploads/2009/03/b48.jpg
Designer - http://www.plumtorics.com/

http://quorvexpixels.net/wp-content/uploads/2009/03/b41.jpg
Designer - http://ferrandokaltz.com/

http://images.pixelhive.com/designs/44195_732292_37774_thumbnail.jpg
Designer- Lumbro Works at Pixel Hive

http://images.pixelhive.com/designs/44195_717529_37774_thumbnail.jpg
Designer - Lumbro Works at Pixel Hive

http://quorvexpixels.net/wp-content/uploads/2009/03/b11.jpg
Designer - http://www.qv7design.com/

http://quorvexpixels.net/wp-content/uploads/2009/03/b16.jpg
Designer - http://www.wobblethistle.com/

Reason: A number of designers have said they want to submit designs and haven't yet done so, we want to give them time.

Reason: We've extended the deadline by 4 days for those who want to submit their designs over the weekend and give ourselves time to judge them

Plastic

Requirements
Nice to have
• The design needs to contain this link: zq.example/Rk7pLx and any other detail that will encourage competition entry. The design will be printed on plastic.
Should not have
• No borders (when plastic cards are punched to shape and size there is movement of 1 - 2mm, borders highlight this movement).

Keep text 3mm away from edges of the cards.

Please don't create designs to be produced on clear/transparent plastic.

```html
<!DOCTYPE html>
<html lang="en">
<head>
<meta charset="utf-8">
<title>Plastic Card Design Competition – Go</title>
<link rel="stylesheet" href="https://fonts.googleapis.com/css2?family=Open+Sans:wght@400&family=Share+Tech+Mono&display=swap">
<style>
  :root {
    --card-bg: #ffffff;
    --arrow-ink: #000000;
    --go-gold: #f2b92a;
    --link-ink: #111111;
  }
  html, body {
    margin: 0;
    padding: 0;
    width: 1200px;
    height: 688px;
    overflow: hidden;
    background: var(--card-bg);
  }
  .card {
    position: relative;
    width: 1200px;
    height: 688px;
    background: var(--card-bg);
  }
  .card-art {
    position: absolute;
    inset: 0;
    width: 1200px;
    height: 688px;
  }
  .arrow-shape {
    fill: var(--arrow-ink);
  }
  .go-label {
    font-family: "Share Tech Mono", monospace;
    font-size: 34px;
    fill: none;
    stroke: var(--go-gold);
    stroke-width: 2.2px;
    letter-spacing: 1px;
  }
  .entry-link {
    font-family: "Open Sans", sans-serif;
    font-size: 15px;
    fill: var(--link-ink);
    letter-spacing: 0.3px;
  }
</style>
</head>
<body>
  <main class="card">
    <svg class="card-art" viewBox="0 0 1200 688" xmlns="http://www.w3.org/2000/svg">
      <defs>
        <path id="link-orbit" d="M 967.9 302.1 A 32 32 0 1 1 970.3 329" fill="none"/>
      </defs>
      <g class="arrow">
        <rect class="arrow-shape" x="182" y="291" width="544" height="45"/>
        <polygon class="arrow-shape" points="724,269 992,313 724,359"/>
      </g>
      <text class="go-label" x="203" y="327">GO</text>
      <text class="entry-link">
        <textPath href="#link-orbit">zq.example/Rk7pLx</textPath>
      </text>
    </svg>
  </main>
</body>
</html>
```